Criação de Capa para Facebook para Consultoria de Negócios
" Palestra, treinamentos e Consultoria em empresas para o crescimento profissional e pessoal dos funcionários "

```html
<!DOCTYPE html>
<html lang="pt-BR">
<head>
<meta charset="UTF-8">
<title>Valentim — Capa Facebook</title>
<link rel="stylesheet" href="https://fonts.googleapis.com/css2?family=Montserrat:wght@200;300;400;500;700;800&display=swap">
<style>
  :root {
    --page: #ffffff;
    --navy-deep: #141c2c;
    --navy: #1f2a40;
    --navy-soft: #34425c;
    --gold: #c9a458;
    --gold-light: #e2c78a;
    --white: #ffffff;
    --muted: #c9cfda;
  }
  * { margin: 0; padding: 0; box-sizing: border-box; }
  html, body { width: 1200px; height: 1200px; overflow: hidden; background: var(--page); }
  body { position: relative; font-family: "Montserrat", sans-serif; }

  .cover {
    position: absolute; left: 0; top: 372px; width: 1200px; height: 456px;
    background: linear-gradient(100deg, var(--navy-deep) 0%, var(--navy) 45%, var(--navy-soft) 75%, var(--navy) 100%);
    overflow: hidden;
  }
  .cover__backdrop {
    position: absolute; left: 0; top: 0; width: 520px; height: 456px;
    background: radial-gradient(ellipse at 30% 30%, rgba(90,110,150,.45), rgba(20,28,44,0) 70%);
  }
  .cover__portrait {
    position: absolute; right: 0; top: 0; width: 390px; height: 456px;
    background: linear-gradient(180deg, #3a4458 0%, #272f40 55%, #161b26 100%);
  }
  .cover__accent {
    position: absolute; left: 0; bottom: 0; width: 8px; height: 120px; background: var(--gold);
  }

  .brand { position: absolute; left: 108px; top: 72px; width: 384px; text-align: center; }
  .brand__mark {
    display: block; width: 96px; height: 96px; margin: 0 auto 30px;
    background: var(--gold);
  }
  .brand__name {
    font-size: 54px; font-weight: 400; letter-spacing: 2px; color: var(--white); line-height: 1;
  }
  .brand__rule { height: 2px; background: var(--gold); margin: 16px 0 14px; }
  .brand__tagline {
    font-size: 18px; font-weight: 400; letter-spacing: 4px; color: var(--white);
  }

  .contacts {
    position: absolute; top: 360px; font-size: 13px; color: var(--muted); line-height: 1.5;
  }
  .contacts--left { left: 40px; }
  .contacts--right { left: 352px; }
  .contact { display: flex; align-items: flex-start; gap: 10px; margin-bottom: 8px; }
  .contact svg { flex: none; width: 18px; height: 18px; margin-top: 1px; }

  .headline { position: absolute; left: 712px; top: 318px; }
  .headline__strong {
    font-size: 44px; font-weight: 800; color: var(--gold-light); letter-spacing: 1px; line-height: 1;
  }
  .headline__light {
    font-size: 46px; font-weight: 200; color: var(--white); letter-spacing: 2px; line-height: 1; margin-top: 10px;
  }
</style>
</head>
<body>
  <section class="cover">
    <div class="cover__backdrop" role="img" aria-label="Foto desfocada de cidade e gráficos financeiros em tons azuis"></div>
    <div class="cover__portrait" role="img" aria-label="Foto do consultor de terno escuro e gravata vermelha, braços cruzados"></div>
    <div class="cover__accent"></div>

    <div class="brand">
      <span class="brand__mark"></span>
      <div class="brand__name">VALENTIM</div>
      <div class="brand__rule"></div>
      <div class="brand__tagline">TREINAMENTO E CONSULTORIA</div>
    </div>

    <div class="contacts contacts--left">
      <div class="contact">
        <svg viewBox="0 0 18 18"><circle cx="9" cy="9" r="8" fill="none" stroke="#c9cfda" stroke-width="1.2"/><path d="M6.3 5.2l1.3 1.6-.7 1c.5 1 1.3 1.8 2.3 2.3l1-.7 1.6 1.3-.8 1.2c-2.6-.4-4.8-2.6-5.2-5.2z" fill="#c9cfda"/></svg>
        <span>(22) 2700 4810</span>
      </div>
      <div class="contact">
        <svg viewBox="0 0 18 18"><circle cx="9" cy="9" r="8" fill="#c9cfda"/><path d="M9 4.5a3 3 0 0 0-3 3c0 2.2 3 6 3 6s3-3.8 3-6a3 3 0 0 0-3-3zm0 4.1a1.1 1.1 0 1 1 0-2.2 1.1 1.1 0 0 1 0 2.2z" fill="#1f2a40"/></svg>
        <span>Av. das Palmeiras - 415<br>Centro - Maricá - RJ - CEP 24900-120</span>
      </div>
    </div>

    <div class="contacts contacts--right">
      <div class="contact">
        <svg viewBox="0 0 18 18"><circle cx="9" cy="9" r="8" fill="none" stroke="#c9cfda" stroke-width="1.2"/><rect x="5" y="6" width="8" height="6" fill="none" stroke="#c9cfda" stroke-width="1"/><path d="M5 6l4 3 4-3" fill="none" stroke="#c9cfda" stroke-width="1"/></svg>
        <span>contato@valentim.com.br</span>
      </div>
      <div class="contact">
        <svg viewBox="0 0 18 18"><circle cx="9" cy="9" r="8" fill="none" stroke="#c9cfda" stroke-width="1.2"/><circle cx="9" cy="9" r="4" fill="none" stroke="#c9cfda" stroke-width="1"/><path d="M5 9h8M9 5c-1.5 2.5-1.5 5.5 0 8M9 5c1.5 2.5 1.5 5.5 0 8" fill="none" stroke="#c9cfda" stroke-width=".8"/></svg>
        <span>www.valentim.com.br</span>
      </div>
    </div>

    <div class="headline">
      <div class="headline__strong">ELEVE</div>
      <div class="headline__light">SEU POTENCIAL</div>
    </div>
  </section>
</body>
</html>
```